E-book cover required. Title is Oda, author Clara J Penrod. Would like large title at top and smaller name at bottom. Book is apocolyptic novel and design needs to reference blood. Simple would be best.

```html
<!DOCTYPE html>
<html lang="en">
<head>
<meta charset="UTF-8">
<title>Oda — Clara J Penrod</title>
<link rel="stylesheet" href="https://fonts.googleapis.com/css2?family=Big+Shoulders+Display:wght@100&family=Petit+Formal+Script&display=swap">
<style>
  :root {
    --paper: #efece6;
    --paper-edge: #ddd8cf;
    --blood-deep: #6e0509;
    --blood-dark: #7d0c14;
    --blood: #b3161f;
    --blood-bright: #d0121a;
    --ink: #111111;
  }
  html, body {
    margin: 0;
    padding: 0;
    width: 750px;
    height: 1200px;
    overflow: hidden;
    background: var(--paper);
  }
  .cover {
    position: relative;
    width: 750px;
    height: 1200px;
    overflow: hidden;
    background: radial-gradient(ellipse at 50% 45%, var(--paper) 55%, var(--paper-edge) 100%);
  }
  .cover-art {
    position: absolute;
    inset: 0;
    width: 750px;
    height: 1200px;
  }
  .title-text {
    font-family: "Big Shoulders Display", "Antonio", sans-serif;
    font-weight: 100;
    font-size: 480px;
  }
  .stop-deep { stop-color: var(--blood-deep); }
  .stop-dark { stop-color: var(--blood-dark); }
  .stop-mid { stop-color: var(--blood); }
  .stop-bright { stop-color: var(--blood-bright); }
  .drop-stem { fill: var(--blood-dark); }
  .author {
    position: absolute;
    left: 0;
    right: 0;
    top: 1086px;
    margin: 0;
    text-align: center;
    font-family: "Petit Formal Script", cursive;
    font-size: 30px;
    font-weight: 400;
    color: var(--ink);
  }
</style>
</head>
<body>
  <main class="cover">
    <svg class="cover-art" viewBox="0 0 750 1200" xmlns="http://www.w3.org/2000/svg" aria-labelledby="book-title">
      <defs>
        <linearGradient id="title-fill" x1="0" y1="0" x2="1" y2="0">
          <stop offset="0" class="stop-dark"/>
          <stop offset="0.5" class="stop-mid"/>
          <stop offset="1" class="stop-dark"/>
        </linearGradient>
        <linearGradient id="drop-fill" x1="0" y1="0" x2="0" y2="1">
          <stop offset="0" class="stop-deep"/>
          <stop offset="0.45" class="stop-dark"/>
          <stop offset="0.55" class="stop-bright"/>
          <stop offset="1" class="stop-mid"/>
        </linearGradient>
      </defs>

      <text id="book-title" class="title-text" y="414" text-anchor="middle" fill="url(#title-fill)"><tspan x="198">O</tspan><tspan x="377">D</tspan><tspan x="562">A</tspan></text>

      <path class="drop-stem" d="M373 410 L381 410 L379 450 L375 450 Z"/>

      <path class="blood-drop" role="img"
            aria-label="Illustration inside the blood drop: a figure in a red dress standing in a red field"
            d="M377 440 C390 525 480 645 480 793 C480 850 434 895 377 895 C320 895 274 850 274 793 C274 645 364 525 377 440 Z"
            fill="url(#drop-fill)"/>

      <path class="drop-shine" d="M460 705 C472 745 474 790 464 830"
            fill="none" stroke="#ffffff" stroke-opacity="0.45" stroke-width="4" stroke-linecap="round"/>
    </svg>

    <p class="author">Clara J Penrod</p>
  </main>
</body>
</html>
```